Business Card Design

Harlow Sun and Electrical is a new company that specializes in solar pv. I need a card with similar attributes to the ones I have attached. I am after a two sided card with the logo on one side and the logo plus info on the other. I would prefer one side to be black and the other to be a colour but am open to suggestions. The colour scheme I was thinking of was blue or green. I plan on spot glossing the logos if that makes any difference. I have attached a file of my logo in a few colours, none of which I am completely sold on so please feel free to change colous to suit.
Thanks.
Contact Information for Business Card
Dorian Harlow, www.hwx-example.net.nz, dorian@hwx-example.net.nz, t. 0508 4 BRIGHT m. 027469318

```html
<!DOCTYPE html>
<html lang="en">
<head>
<meta charset="utf-8">
<title>Harlow Sun and Electrical – Business Card</title>
<link rel="stylesheet" href="https://fonts.googleapis.com/css2?family=Montserrat:wght@600&family=Open+Sans:wght@400;600&display=swap">
<style>
  :root {
    --stage: #e7e3dc;
    --green-light: #b9e866;
    --green: #95d43c;
    --green-deep: #72b82a;
    --black: #141414;
    --black-soft: #262626;
    --ink: #1b1b1b;
    --ink-muted: #3a3a3a;
  }
  * { margin: 0; padding: 0; box-sizing: border-box; }
  html, body {
    width: 1200px; height: 1023px; overflow: hidden;
    background: var(--stage);
  }
  .stage {
    position: relative; width: 1200px; height: 1023px;
    display: flex; flex-direction: column; align-items: center; justify-content: center; gap: 60px;
  }
  .card {
    position: relative; width: 700px; height: 400px;
    border-radius: 30px; overflow: hidden;
    box-shadow: 0 10px 30px rgba(0,0,0,.18);
  }
  .card-front { background: var(--black); }
  .card-front .shapes { position: absolute; inset: 0; }

  .brand-name {
    font-family: "Montserrat", sans-serif; font-weight: 600;
    text-transform: uppercase; line-height: 1.15; letter-spacing: .04em;
  }
  .front-brand {
    position: absolute; left: 34px; top: 140px; width: 270px;
    font-size: 30px; color: var(--ink);
  }

  .person {
    position: absolute; left: 415px; top: 232px;
    font-family: "Open Sans", sans-serif; color: var(--ink);
  }
  .person-name { font-size: 25px; font-weight: 400; letter-spacing: .03em; text-transform: uppercase; }
  .person-role { font-size: 15px; color: var(--ink-muted); margin-top: 4px; }

  .contact-list {
    position: absolute; left: 455px; top: 36px; list-style: none;
    font-family: "Open Sans", sans-serif; font-size: 15px; color: var(--ink);
  }
  .contact-list li { display: flex; align-items: center; gap: 8px; height: 24px; }
  .contact-icon { width: 15px; height: 15px; flex: none; }

  .front-web {
    position: absolute; left: 415px; bottom: 18px;
    font-family: "Open Sans", sans-serif; font-size: 14px; font-weight: 600;
    letter-spacing: .12em; color: var(--green);
  }

  .card-back {
    background: linear-gradient(135deg, var(--black-soft) 0%, var(--black) 55%, #0c0c0c 100%);
    display: flex; flex-direction: column; align-items: center; justify-content: center; gap: 22px;
  }
  .back-brand { font-size: 38px; color: var(--green); text-align: center; }
  .back-web {
    font-family: "Open Sans", sans-serif; font-size: 15px; font-weight: 600;
    letter-spacing: .16em; color: var(--green);
  }
</style>
</head>
<body>
<main class="stage">
  <section class="card card-front" aria-label="Card front">
    <svg class="shapes" width="700" height="400" viewBox="0 0 700 400" aria-hidden="true">
      <defs>
        <linearGradient id="greenFill" x1="0" y1="0" x2="1" y2="1">
          <stop offset="0" stop-color="var(--green-light)"/>
          <stop offset="1" stop-color="var(--green-deep)"/>
        </linearGradient>
      </defs>
      <path class="panel-logo" d="M0 0 H240 A90 90 0 0 1 330 90 V400 H0 Z" fill="url(#greenFill)"/>
      <path class="panel-info" d="M380 0 H700 V350 H470 A90 90 0 0 1 380 260 Z" fill="url(#greenFill)"/>
    </svg>

    <p class="brand-name front-brand">Harlow Sun and Electrical</p>

    <ul class="contact-list">
      <li>
        <svg class="contact-icon" viewBox="0 0 16 16" aria-hidden="true"><rect width="16" height="16" rx="3" fill="#1b1b1b"/><path d="M5 4c1 0 1.5 2 1 2.5l-.6.6c.5 1.2 1.3 2 2.5 2.5l.6-.6c.5-.5 2.5 0 2.5 1 0 1-1 1.5-1.8 1.5C6.5 11.5 4.5 9.5 4 6 3.8 5 4.2 4 5 4z" fill="#b9e866"/></svg>
        <span>0508 4 BRIGHT</span>
      </li>
      <li>
        <svg class="contact-icon" viewBox="0 0 16 16" aria-hidden="true"><rect width="16" height="16" rx="3" fill="#1b1b1b"/><rect x="5" y="3" width="6" height="10" rx="1" fill="#b9e866"/><rect x="6" y="4.3" width="4" height="6" fill="#1b1b1b"/></svg>
        <span>027469318</span>
      </li>
      <li>
        <svg class="contact-icon" viewBox="0 0 16 16" aria-hidden="true"><rect width="16" height="16" rx="3" fill="#1b1b1b"/><rect x="3.5" y="5" width="9" height="6.5" fill="#b9e866"/><path d="M3.5 5 L8 8.6 L12.5 5" fill="none" stroke="#1b1b1b" stroke-width="1"/></svg>
        <span>dorian@hwx-example.net.nz</span>
      </li>
    </ul>

    <div class="person">
      <p class="person-name">Dorian Harlow</p>
      <p class="person-role">Director</p>
    </div>

    <p class="front-web">www.hwx-example.net.nz</p>
  </section>

  <section class="card card-back" aria-label="Card back">
    <p class="brand-name back-brand">Harlow Sun<br>and Electrical</p>
    <p class="back-web">www.hwx-example.net.nz</p>
  </section>
</main>
</body>
</html>
```